9x12 Business Brochure, 3 fold, for Internet Marketing Company

I'd like to have a brochure designed for my Internet marketing company. I have the content all ready, 10 Internet Marketing Myths, which you can see here: http://www.steadfernwebreach.com/common-internet-marketing-myths/. I'm looking for something creative and business to business. The company is all about Internet marketing. I like the "http://" header I use at our website. People like it too and identify with it. Audience is business owners 35 to 55 years old. I use blue at my website. I *think* I would like the cover page (front page) to open with some attention grabbing text, that basically takes most of the front page of the brochure. It would probably say: "I Can Help You Get BETTER RESULTS from Your Website, More Traffic, TOP RANKINGS at Zorvik, More Leads and MORE SALES. But first you'll have to avoid these common Internet marketing myths..." The inside pages would have the content from above (the 10 myths). The back page would have testimonials that I can provide. And the inside folded in page (or what I call the inside folded in page) would have a list of services. I think I want the dimensions 12x9 which is a larger sized, three-fold brochure.

Target Market(s)

I use this brochure to send to business owners and managers to show them I know what I'm talking about and and expert. See attachment for content.

Industry/Entity Type

Marketing

Requirements
Should not have
• No clipart. Probably not illustrations. Photos. The "http://" used at the site is something people "connect" with and get that this is about Internet marketing.

```html
<!DOCTYPE html>
<html lang="en">
<head>
<meta charset="utf-8">
<title>Common Internet Marketing Myths – Brochure</title>
<link rel="stylesheet" href="https://fonts.googleapis.com/css2?family=Architects+Daughter&family=Didact+Gothic&family=Montserrat:wght@700&family=Open+Sans:wght@700&display=swap">
<style>
  :root{
    --backdrop:#e6e8eb;
    --paper:#ffffff;
    --fold:#d9dce0;
    --ink:#141414;
    --blue-strong:#1b4f9c;
    --blue-soft:#3a6fb4;
    --blue-script:#1d4a94;
    --muted:#333;
  }
  *{box-sizing:border-box;margin:0;padding:0}
  html,body{width:1200px;height:638px;overflow:hidden;background:var(--backdrop)}
  .stage{position:relative;width:1200px;height:638px}
  .panel{position:absolute;top:19px;width:267px;height:600px;background:var(--paper);
    box-shadow:0 2px 8px rgba(0,0,0,.18)}
  .cover{left:26px;padding:52px 22px 24px 26px}
  .spread{position:absolute;top:19px;left:333px;width:801px;height:600px;background:var(--paper);
    box-shadow:0 2px 8px rgba(0,0,0,.18);display:flex}
  .spread .column{width:267px;height:600px;padding:18px 15px 14px}
  .spread .column + .column{border-left:1px solid var(--fold)}

  /* cover */
  .headline{font-family:"Didact Gothic",sans-serif;color:var(--blue-soft);font-size:21px;line-height:1.12}
  .headline .thin{display:block}
  .headline .loud{display:block;font-family:"Montserrat",sans-serif;font-weight:700;
    color:var(--blue-strong);font-size:22px;letter-spacing:.3px;line-height:1.08}
  .teaser{margin-top:34px;font-family:"Architects Daughter",cursive;color:var(--ink);
    font-size:13.5px;line-height:1.35;text-align:center}
  .teaser svg{vertical-align:-3px}
  .sender{position:absolute;left:26px;bottom:30px;font-family:"Didact Gothic",sans-serif;
    font-size:11px;color:var(--muted);line-height:1.4}

  /* myths */
  .myth + .myth{margin-top:11px}
  .myth-title{font-family:"Architects Daughter",cursive;color:var(--blue-script);font-size:12.5px;
    line-height:1.12;text-align:center;font-weight:400;margin-bottom:5px}
  .myth-body{font-family:"Open Sans",sans-serif;font-weight:700;font-size:7.5px;line-height:1.36;
    color:var(--ink);text-align:justify}
</style>
</head>
<body>
<main class="stage">

  <section class="panel cover" aria-label="Front cover">
    <h1 class="headline">
      <span class="thin">I Can Help You Get</span>
      <span class="loud">BETTER</span>
      <span class="loud">RESULTS</span>
      <span class="thin">from Your website,</span>
      <span class="thin">More Traffic,</span>
      <span class="loud">TOP</span>
      <span class="loud">RANKINGS</span>
      <span class="thin">with Zorvik,</span>
      <span class="thin">More Inquiries, and</span>
      <span class="loud">MORE SALES</span>
    </h1>
    <p class="teaser">But first you'll need to avoid<br>these Common<br>Internet Marketing Myths...
      <svg width="12" height="16" viewBox="0 0 12 16" aria-hidden="true"><path d="M1 1 L1 13 L4 10 L6.5 15 L8.5 14 L6 9 L10.5 9 Z" fill="#fff" stroke="#222" stroke-width="1"/></svg>
    </p>
    <p class="sender">Dana Holloway Consulting (.com)<br>(555) 014-2270</p>
  </section>

  <section class="spread" aria-label="Inside spread">
    <div class="column">
      <article class="myth">
        <h2 class="myth-title">Myth # 1 If You Build It,<br>Traffic Will Come</h2>
        <p class="myth-body">If you are in any competitive category of products or services, or in a geographically competitive marketplace, the chances that you can build a website, develop the traffic, and manage your ongoing online marketing ALL BY YOURSELF are less than one in ten. Put another way, DIY has a 90% chance of FAILURE.</p>
      </article>
      <article class="myth">
        <h2 class="myth-title">Myth # 2 Top Rankings<br>Are All You'll Need</h2>
        <p class="myth-body">This is a common misconception, and costly too. Many believe search engines and organic ranking is all you need for online success. A top ranked website is a very good thing and it can drive a lot of qualified traffic, but for a new website, it can take months, or years, to reach top positioning — if you can get it at all. The answer is a multi-pronged approach to building traffic, including buying advertising, pay-per-click advertising (PPC), integration of your offline advertising with your online marketing, blogging, social media, and of course, search engine optimization (SEO).</p>
      </article>
      <article class="myth">
        <h2 class="myth-title">Myth # 3 All Traffic is Good</h2>
        <p class="myth-body">Not true! To get real results from your website, inquiries, phone calls, and sales, you'll need to find and attract QUALIFIED traffic – people who are actually getting married and who are ready to purchase your products and services.</p>
      </article>
    </div>

    <div class="column">
      <article class="myth">
        <h2 class="myth-title">Myth # 4 Hits Are A Good Measure of Success</h2>
        <p class="myth-body">Wrong! If you are measuring "hits" you're not even in the game. A "hit" is a technical term that describes activity on a hosting server. Unfortunately, most webmasters use this term casually and it is interpreted to mean you have lots of traffic. Hits are not real people. Real people who visit your website are logged as "visitor sessions."</p>
      </article>
      <article class="myth">
        <h2 class="myth-title">Myth # 5 You Can Do This All Yourself</h2>
        <p class="myth-body">If you are in any competitive category of products or services, or in a geographically competitive marketplace, the chances that you can build a website, develop the traffic, and manage your ongoing online marketing ALL BY YOURSELF are less than one in ten. Put another way, DIY has a 90% chance of FAILURE.</p>
      </article>
      <article class="myth">
        <h2 class="myth-title">Myth # 6 It's Easy to Get Traffic<br>From Search Engines</h2>
        <p class="myth-body">In today's competitive marketplace it is more difficult than ever to get top ranking with Zorvik, Quellfind, or Sirrow. It is very likely going to take six to twelve months to see your website achieve a top ranked position for any competitive keyword/keyword phrase that people are searching for – and that's only if you have SEO expertise. If your website is new it will take longer.</p>
      </article>
      <article class="myth">
        <h2 class="myth-title">Myth # 7 Submitting Your Website to<br>Search Engines Actually Works</h2>
        <p class="myth-body">If you are in any competitive category of products or services, or in a geographically competitive marketplace, the chances that you can build a website, develop the traffic, and manage your ongoing online marketing ALL BY YOURSELF are less than one in ten. Put another way, DIY has a 90% chance of FAILURE.</p>
      </article>
    </div>

    <div class="column">
      <article class="myth">
        <h2 class="myth-title">Myth # 8 Search Engine Optimization Is Easy</h2>
        <p class="myth-body">Search engine optimization is not difficult but there is a lot to it. There are dozens of different variables that must be perfectly managed. Each of these falls into one of two categories: "on-page" variables or "off-page" variables. Add to this hundreds of so-called "experts" and their advice (which is incorrect, incomplete, or misleading), and it's pretty hard to call the search engine optimization process easy. Getting top ranked is even more challenging when a competitor has hired a reputable SEO expert to help them with their website and Internet marketing strategy.</p>
      </article>
      <article class="myth">
        <h2 class="myth-title">Myth # 9 Meta-Tags Are The Key To A<br>Top Ranked Website</h2>
        <p class="myth-body">Meta-tags are specific lines of programming code that appear behind-the-scenes at your website. Search engines see them but your visitors do not. Search engines use meta-tags as one of the factors in determining page relevancy. Zorvik's algorithm tries to show the most relevant pages for a search on a search engine results page (SERP). Meta-tags are still important, but only one of more than two dozen factors related to the overall search engine optimization of your website.</p>
      </article>
      <article class="myth">
        <h2 class="myth-title">Myth # 10 Your Webmaster/Programmer Can<br>Help You With Your Internet Marketing</h2>
        <p class="myth-body">Graphics design, programming code, and page layout are very different from Internet marketing. In most cases, (90% of the time) a webmaster / programmer will not be able to give you the appropriate advice or support to effectively promote and market your website online.</p>
      </article>
    </div>
  </section>

</main>
</body>
</html>
```